Take my logo and make me some cool looking business cards

I've got a logo that we've trademarked so you can't change the logo but you can change it's color combo and find a fun way to incorporate it into a new business card design that is fresh, stylish, and can be applied to some cool medium cost materials (plastic, wood, metal, etc). Basically, we're looking for business cards that stand out in a good way.
Updates
Here's the logo we're currently using:
Thanks to everyone that has submitted designs. We've narrowed down to the top 4 designs and tried to eliminate old versions or designs that just didn't match our vision as quickly as we could. We don't plan on keeping this open for the full 9 days; we plan on selecting a design in the next 48 hours; with the goal of having something in the hands of a printer, preferably plastic printer, by Thursday AM Pacific Time.
Industry/Entity Type
Business
Requirements
Must have
- must include our existing logo

```html
<!DOCTYPE html>
<html lang="en">
<head>
<meta charset="utf-8">
<title>Waymark Business Card</title>
<link rel="stylesheet" href="https://fonts.googleapis.com/css2?family=Open+Sans:wght@700&display=swap">
<style>
  :root {
    --backdrop: #bdbec0;
    --wood-light: #f3d08f;
    --wood-mid: #ebbd6c;
    --wood-deep: #e0a955;
    --ink: #3f2b1d;
  }
  html, body {
    margin: 0;
    padding: 0;
    width: 1200px;
    height: 750px;
    overflow: hidden;
    background: var(--backdrop);
    font-family: "Open Sans", Arial, sans-serif;
  }
  .stage {
    position: relative;
    width: 1200px;
    height: 750px;
  }
  .business-card {
    position: absolute;
    left: 246px;
    top: 102px;
    width: 754px;
    height: 430px;
    overflow: hidden;
    color: var(--ink);
  }
  .wood-surface {
    position: absolute;
    inset: 0;
    background: linear-gradient(180deg,
      var(--wood-light) 0%,
      var(--wood-mid) 30%,
      var(--wood-light) 50%,
      var(--wood-deep) 75%,
      var(--wood-mid) 100%);
  }
  .brand-name {
    position: absolute;
    left: 0;
    right: 0;
    top: 98px;
    margin: 0;
    text-align: center;
    font-size: 92px;
    font-weight: 700;
    letter-spacing: 4px;
    line-height: 1;
  }
  .person {
    position: absolute;
    right: 421px;
    top: 252px;
    text-align: right;
    margin: 0;
  }
  .person-name {
    display: block;
    font-size: 30px;
    font-weight: 700;
    line-height: 1;
  }
  .person-title {
    display: block;
    margin-top: 30px;
    font-size: 23px;
    font-weight: 700;
    line-height: 1;
  }
  .contact {
    position: absolute;
    left: 386px;
    top: 254px;
    margin: 0;
    font-style: normal;
    font-size: 21px;
    font-weight: 700;
    line-height: 32px;
  }
</style>
</head>
<body>
  <main class="stage">
    <section class="business-card">
      <div class="wood-surface" role="img" aria-label="Light pine wood grain surface"></div>
      <h1 class="brand-name">WAYMARK</h1>
      <p class="person">
        <span class="person-name">Jordan Hale</span>
        <span class="person-title">CEO</span>
      </p>
      <address class="contact">
        418 Marlow Avenue<br>
        Pine Cove, CA 94120<br>
        +140 555 01234
      </address>
    </section>
  </main>
</body>
</html>
```